Wild Mo's Wine Label Project

We need a new entry level wine label called "Wild Mo's" for a range of wines we are developing from inland Australia. Our company is made up of three youngish guys who live hard and love taking the mickey. Wild Mo is Wild Moss - the largest and loudest of the three partners (and ideally this label will take the mickey out of him). We've grown the grapes ourselves for this first release which will be a 2012 Pinot Gris. Wine style is dry, young, fresh and contemporary and pitched at the sub AUD $10 retail price point. The package will be flint (clear) claret shape bottle with plain screwcap (colour matched to suit the winning label design).

I've attached a couple of photos of Wild Moss to give you some idea of his presence and persona.

Target Market(s)

Semi educated 25 - 40 year old wine drinkers. Skewed towards females.

Industry/Entity Type

Retail

Requirements
Should not have
• Anything traditional or old fashioned

```html
<!DOCTYPE html>
<html lang="en">
<head>
<meta charset="utf-8">
<title>Wild Mo's – Label Design</title>
<link href="https://fonts.googleapis.com/css2?family=Stardos+Stencil:wght@700&family=Arimo:wght@400&display=swap" rel="stylesheet">
<style>
  :root {
    --brand-plum: #5b0c3d;
    --bottle-top: #2a1a22;
    --bottle-body: #3a1428;
    --bottle-edge: #1c0f16;
    --label-charcoal: #454545;
    --neck-dark: #262626;
    --art-dark: #2b2b2b;
    --paper: #ffffff;
    --note-bg: #000000;
    --note-text: #ffffff;
  }
  * { box-sizing: border-box; margin: 0; padding: 0; }
  html, body { width: 837px; height: 1200px; overflow: hidden; background: var(--paper); }
  .canvas { position: relative; width: 837px; height: 1200px; background: var(--paper); font-family: "Arimo", Helvetica, Arial, sans-serif; }

  .brand-mark {
    position: absolute; left: 40px; top: 70px;
    display: flex; align-items: center; gap: 16px;
  }
  .brand-mark__dot { width: 34px; height: 34px; border-radius: 50%; background: var(--brand-plum); }
  .brand-mark__name {
    font-family: "Stardos Stencil", "Arial Black", sans-serif; font-weight: 700;
    font-size: 58px; color: var(--brand-plum); letter-spacing: 1px; white-space: nowrap;
  }

  /* Bottle stand-in: flat silhouette carrying both labels */
  .bottle { position: absolute; top: 232px; width: 240px; height: 884px; }
  .bottle--charcoal { left: 256px; }
  .bottle--plum { left: 536px; }
  .bottle__form { position: absolute; inset: 0; }
  .bottle__neck {
    position: absolute; left: 76px; top: 0; width: 88px; height: 240px;
    background: linear-gradient(90deg, var(--bottle-edge), var(--bottle-top) 45%, var(--bottle-edge));
    border-radius: 10px 10px 0 0;
  }
  .bottle__shoulder {
    position: absolute; left: 0; top: 200px; width: 240px; height: 684px;
    background: linear-gradient(90deg, var(--bottle-edge), var(--bottle-body) 40%, var(--bottle-edge));
    border-radius: 90px 90px 16px 16px;
  }

  .neck-label {
    position: absolute; left: 76px; top: 38px; width: 88px; height: 106px;
    background: var(--neck-dark);
  }
  .neck-label__name {
    position: absolute; left: 6px; top: 8px;
    font-family: "Stardos Stencil", "Arial Black", sans-serif; font-weight: 700;
    font-size: 13px; color: var(--brand-plum); white-space: nowrap;
  }
  .neck-label__art {
    position: absolute; left: 6px; top: 28px; width: 44px; height: 62px;
    background: var(--brand-plum); border-radius: 6px; opacity: 0.9;
  }
  .neck-label__year {
    position: absolute; right: 6px; top: 66px; font-size: 15px; color: var(--brand-plum);
  }

  .body-label {
    position: absolute; left: 5px; top: 556px; width: 230px; height: 288px;
    border-radius: 8px; overflow: hidden;
  }
  .body-label--charcoal { background: var(--label-charcoal); }
  .body-label--plum { background: var(--brand-plum); }
  .body-label__art {
    position: absolute; left: 0; top: 14px; width: 230px; height: 150px;
    background: linear-gradient(200deg, rgba(43,43,43,0.35), rgba(30,30,30,0.75));
    clip-path: polygon(8% 0, 100% 0, 100% 70%, 40% 100%, 8% 80%);
  }
  .body-label__name {
    position: absolute; left: 0; right: 0; top: 188px; text-align: center;
    font-family: "Stardos Stencil", "Arial Black", sans-serif; font-weight: 700;
    font-size: 34px; line-height: 1; white-space: nowrap;
  }
  .body-label__year {
    position: absolute; right: 14px; top: 222px; font-size: 24px; line-height: 1;
  }
  .body-label--charcoal .body-label__name,
  .body-label--charcoal .body-label__year { color: var(--brand-plum); }
  .body-label--plum .body-label__name,
  .body-label--plum .body-label__year { color: var(--art-dark); }

  .spec-swatch {
    position: absolute; left: 24px; top: 1094px; width: 42px; height: 40px;
    background: var(--brand-plum); border-radius: 3px;
    color: var(--note-text); font-size: 8px; line-height: 12px; padding: 3px 4px;
  }
  .spec-font {
    position: absolute; left: 24px; top: 1137px; width: 72px; height: 50px;
    background: var(--note-bg); color: var(--note-text);
    font-size: 8px; line-height: 11px; padding: 8px 6px;
  }
</style>
</head>
<body>
<main class="canvas">
  <div class="brand-mark">
    <span class="brand-mark__dot"></span>
    <span class="brand-mark__name">WILD MO'S</span>
  </div>

  <article class="bottle bottle--charcoal">
    <div class="bottle__form" role="img" aria-label="Dark claret bottle carrying the charcoal label">
      <div class="bottle__neck"></div>
      <div class="bottle__shoulder"></div>
    </div>
    <div class="neck-label">
      <span class="neck-label__name">WILD MO'S</span>
      <div class="neck-label__art" role="img" aria-label="Small grape cluster illustration in plum"></div>
      <span class="neck-label__year">2012</span>
    </div>
    <section class="body-label body-label--charcoal">
      <div class="body-label__art" role="img" aria-label="Grape cluster and vine leaf illustration in dark grey"></div>
      <span class="body-label__name">WILD MO'S</span>
      <span class="body-label__year">2012</span>
    </section>
  </article>

  <article class="bottle bottle--plum">
    <div class="bottle__form" role="img" aria-label="Dark claret bottle carrying the plum label">
      <div class="bottle__neck"></div>
      <div class="bottle__shoulder"></div>
    </div>
    <div class="neck-label">
      <span class="neck-label__name">WILD MO'S</span>
      <div class="neck-label__art" role="img" aria-label="Small grape cluster illustration in plum"></div>
      <span class="neck-label__year">2012</span>
    </div>
    <section class="body-label body-label--plum">
      <div class="body-label__art" role="img" aria-label="Grape cluster and vine leaf illustration in dark grey"></div>
      <span class="body-label__name">WILD MO'S</span>
      <span class="body-label__year">2012</span>
    </section>
  </article>

  <div class="spec-swatch">R: 91<br>G: 12<br>B: 61</div>
  <div class="spec-font">FONT:<br>ARMY<br>HELVETICA</div>
</main>
</body>
</html>
```